One Page flat design for Car Classified Site

I'm looking for a flat design that that is very simple on the eye but with style. I need it to have a footer for some links etc, and the header needs a new feel but nothing to major.
This one page design is needed for the main page of the classified site...after this page is correct then all the other pages need to be designed to follow a similar style (new work).
I want more emphasis on the text rather than the images as a lot of users don't add images of the vehicles.
Attached is a mock up of the information and rough layout.
Motorbayhub.com is a classified site for car dealers only, I've also attached how the main competitions site looks.
Target Market(s)
Middle aged men, these guys are car dealers so it needs to be basic and easy for them as they aren't techie types.
Industry/Entity Type
Work
Number of Pages Required
1 page
Font styles to use
Look and feel

```html
<!DOCTYPE html>
<html lang="en">
<head>
<meta charset="utf-8">
<title>Motorbayhub.com – Car Classifieds</title>
<link href="https://fonts.googleapis.com/css2?family=Oswald:wght@400;600;700&family=Roboto:wght@400;500;700&display=swap" rel="stylesheet">
<style>
:root{
  --yellow:#f5d30f;
  --ink:#1b1b1b;
  --dark:#222222;
  --darker:#161616;
  --line:#d9d9d9;
  --text:#333333;
  --muted:#777777;
  --white:#ffffff;
}
*{box-sizing:border-box;margin:0;padding:0}
html,body{width:1200px;height:2251px;overflow:hidden;background:var(--white)}
body{font-family:"Roboto",Arial,sans-serif;color:var(--text);font-size:12px}
.page{position:relative;width:1200px;height:2251px;overflow:hidden}
.abs{position:absolute}
.heading{font-family:"Oswald","Arial Narrow",sans-serif;font-weight:700;font-style:italic;text-transform:uppercase;color:var(--ink)}

/* header */
.site-header{position:absolute;left:0;top:0;width:1200px;height:85px;background:var(--white);z-index:3}
.brand{position:absolute;left:160px;top:24px;font-family:"Oswald",sans-serif;font-weight:700;font-style:italic;font-size:27px;color:var(--ink);text-transform:uppercase;letter-spacing:.3px}
.main-nav{position:absolute;left:509px;top:25px;display:flex;font-family:"Oswald",sans-serif;font-style:italic;font-size:11px;text-transform:uppercase;color:#555}
.main-nav a{color:inherit;text-decoration:none;padding:0 10px;position:relative}
.main-nav a + a::before{content:"//";position:absolute;left:-6px;color:#aaa;font-size:9px}
.main-nav a.active{color:var(--ink);border-bottom:2px solid var(--yellow);padding-bottom:4px}
.account-tab{position:absolute;left:900px;top:0;width:136px;height:68px}
.account-tab span{position:absolute;left:22px;top:25px;font-family:"Oswald",sans-serif;font-style:italic;font-size:12px;color:var(--ink);text-transform:uppercase}

/* hero */
.hero{position:absolute;left:0;top:70px;width:1200px;height:430px;background:radial-gradient(ellipse at 30% 55%,#4a4a4a 0%,#222 45%,#0c0c0c 100%)}
.filter-box{position:absolute;left:198px;top:214px;width:800px;height:151px;background:rgba(10,10,10,.82)}
.filter-box h2{position:absolute;left:18px;top:12px;font-size:21px;color:var(--white);text-transform:none}
.field{position:absolute;height:28px;background:var(--white);font-size:10px;color:#888;padding:8px 7px;border:1px solid #ccc}
.select{background:#f2f2f2}
.select::after{content:"";position:absolute;right:0;top:0;width:26px;height:26px;background:#5a5a5a}
.select::before{content:"";position:absolute;right:9px;top:11px;border:4px solid transparent;border-top-color:#fff;z-index:1}
.btn{position:absolute;background:var(--yellow);color:var(--ink);font-size:11px;font-weight:500;display:flex;align-items:center;justify-content:center;gap:5px}

/* vehicles */
.section-title{position:absolute;left:0;width:1200px;text-align:center;font-size:23px}
.card{position:absolute;top:671px;width:279px;height:405px;border:1px solid var(--line);background:var(--white)}
.card .photo{position:absolute;left:0;top:0;width:277px;height:219px;background:linear-gradient(180deg,#7aa04a 0%,#b9c9a0 40%,#e8e8e8 60%,#6c6c6c 100%)}
.card .photo.street{background:linear-gradient(180deg,#9aa4ad 0%,#d2d6da 45%,#f1f1f1 62%,#555 100%)}
.card .bid{position:absolute;left:0;top:190px;width:277px;height:29px;background:rgba(0,0,0,.85);color:var(--white);font-size:11.5px;padding:8px 9px}
.card h3{position:absolute;left:15px;top:233px;font-size:13px;font-weight:700;color:var(--ink)}
.specs{position:absolute;left:15px;top:254px;width:250px;display:grid;grid-template-columns:1fr 1fr;row-gap:5px;font-size:9.5px;color:var(--muted)}
.card .deal{position:absolute;left:0;top:315px;width:277px;height:88px;background:#f3f3f3;border-top:1px solid var(--line)}
.deal h4{position:absolute;left:15px;top:12px;font-size:13px;font-weight:700;color:var(--ink)}
.deal p{position:absolute;left:15px;font-size:12px;color:var(--text)}
.deal .btn{left:199px;top:50px;width:64px;height:20px;font-size:10px}

/* promo band */
.promo{position:absolute;left:0;top:1119px;width:1200px;height:225px;background:linear-gradient(180deg,#2a2a2a,#1a1a1a)}
.promo h2{position:absolute;top:48px;width:1200px;text-align:center;font-size:23px;color:var(--yellow)}
.promo p{position:absolute;left:170px;top:85px;width:860px;text-align:center;font-size:10px;line-height:13px;color:#e6e6e6}
.contact-box{position:absolute;top:133px;width:172px;height:48px;border:1px solid #666;background:#151515;color:var(--white);text-align:center;font-family:"Oswald",sans-serif;font-size:12px;padding-top:6px;line-height:18px}
.contact-box .val{color:var(--yellow);font-family:"Roboto",sans-serif;font-size:11px;display:flex;align-items:center;justify-content:center;gap:5px}

/* contact form */
.form-label{position:absolute;left:160px;top:1433px;font-family:"Oswald",sans-serif;font-size:19px;color:var(--ink);text-transform:uppercase}
.input{position:absolute;left:160px;width:430px;height:31px;background:#efefef;border:1px solid var(--line);font-size:10px;color:#777;padding:10px 10px}
.textarea{left:610px;top:1466px;height:79px;width:430px}

/* testimonial */
.testimonial{position:absolute;left:0;top:1639px;width:1200px;height:225px;background:linear-gradient(90deg,var(--yellow) 0%,#f2d43a 60%,#e8cf45 100%)}
.testimonial h2{position:absolute;top:38px;width:1200px;text-align:center;font-size:23px}
.quote-mark{position:absolute;left:218px;top:82px;font-family:"Oswald",sans-serif;font-size:46px;color:#7a6a10;line-height:1}
.testimonial p{position:absolute;left:243px;top:90px;width:775px;text-align:center;font-size:10px;line-height:14px;color:#333}
.testimonial .who{top:166px;font-size:10px;line-height:16px;color:#222}

/* footer */
.footer-top{position:absolute;left:0;top:1932px;width:1200px;height:256px}
.footer-brand{position:absolute;left:160px;top:1992px;font-family:"Oswald",sans-serif;font-weight:700;font-style:italic;font-size:27px;color:var(--yellow);text-transform:uppercase}
.footer-text{position:absolute;left:160px;top:2040px;width:443px;font-size:10.5px;line-height:15px;color:#ddd}
.footer-heading{position:absolute;left:664px;top:2004px;width:376px;font-family:"Oswald",sans-serif;font-size:18px;color:var(--white);text-transform:uppercase;border-bottom:1px solid #555;padding-bottom:6px}
.f-input{position:absolute;top:2049px;height:31px;background:#efefef;font-size:10px;color:#666;padding:10px}
.signup-note{position:absolute;left:757px;top:2092px;width:180px;font-size:10px;line-height:14px;color:#ddd}
.bottom-bar{position:absolute;left:0;top:2188px;width:1200px;height:63px;background:var(--darker);border-top:1px solid #333}
.foot-nav{position:absolute;left:160px;top:17px;display:flex;font-size:10px;color:#bbb;text-transform:uppercase}
.foot-nav a{color:inherit;text-decoration:none;padding:0 8px;border-left:1px solid #555}
.foot-nav a:first-child{padding-left:0;border-left:0}
.copyright{position:absolute;left:160px;top:36px;font-size:10px;color:#999}
.social{position:absolute;left:918px;top:14px;display:flex;gap:11px}
.social span{display:block;width:23px;height:23px;background:#5c5c5c}
</style>
</head>
<body>
<div class="page">

  <header class="site-header">
    <div class="brand">Motorbayhub.com</div>
    <nav class="main-nav">
      <a class="active" href="#">Home</a>
      <a href="#">Who we are</a>
      <a href="#">Cars for sale</a>
      <a href="#">News &amp; Reviews</a>
      <a href="#">Help</a>
    </nav>
    <div class="account-tab">
      <svg width="136" height="68" viewBox="0 0 136 68"><polygon points="0,0 136,0 136,68 10,68" fill="var(--yellow)"/></svg>
      <span>Sign in / Sign up</span>
    </div>
  </header>

  <section class="hero" role="img" aria-label="Dark photograph of a black luxury saloon in a tunnel"></section>
  <svg class="abs" style="left:0;top:452px" width="1200" height="50" viewBox="0 0 1200 50"><polygon points="740,50 790,20 1200,8 1200,50" fill="var(--white)"/></svg>

  <div class="filter-box">
    <h2 class="heading">Filter Cars</h2>
    <div class="field select" style="left:18px;top:65px;width:189px">Select Manufacturer</div>
    <div class="field select" style="left:216px;top:65px;width:178px">Select Model</div>
    <div class="field select" style="left:410px;top:65px;width:184px">Select Price</div>
    <div class="field select" style="left:608px;top:65px;width:184px">Select Year</div>
    <div class="field select" style="left:18px;top:106px;width:189px">Select Body type</div>
    <div class="field" style="left:216px;top:106px;width:178px">Keywords</div>
    <div class="btn" style="left:410px;top:106px;width:98px;height:28px">Filter Vehicles
      <svg width="9" height="8" viewBox="0 0 9 8"><path d="M1 1l3 3-3 3M5 1l3 3-3 3" stroke="#1b1b1b" stroke-width="1.4" fill="none"/></svg></div>
  </div>

  <div class="abs" style="left:0;top:556px;width:1200px;height:1px;background:#e6e6e6"></div>
  <h2 class="section-title heading" style="top:596px">Latest Vehicles</h2>

  <article class="card" style="left:160px">
    <div class="photo" role="img" aria-label="Photo of a white sports coupe on a tree-lined road"></div>
    <div class="bid">Buy it now for £13750 or please bid &raquo;</div>
    <h3>Velmont Tessa</h3>
    <div class="specs"><span>2014 - 64</span><span>White</span><span>86000 Miles</span><span>Ridgeway Cars</span><span>Automatic</span><span>127 Miles Away</span></div>
    <div class="deal"><h4>Trying to deal my customer</h4><p style="top:34px">Trade Price : £15,750</p><p style="top:52px">Retail Price : £17,750</p><div class="btn">More Info</div></div>
  </article>

  <article class="card" style="left:461px">
    <div class="photo street" role="img" aria-label="Photo of a white estate car parked on a street"></div>
    <div class="bid">Buy it now for £13750 or please bid &raquo;</div>
    <h3>Harlow</h3>
    <div class="specs"><span>2014 - 64</span><span>White</span><span>86000 Miles</span><span>Ridgeway Cars</span><span>Automatic</span><span>127 Miles Away</span></div>
    <div class="deal"><h4>Trying to deal my customer</h4><p style="top:34px">Trade Price : £15,750</p><p style="top:52px">Retail Price : £17,750</p><div class="btn">More Info</div></div>
  </article>

  <article class="card" style="left:763px">
    <div class="photo" role="img" aria-label="Photo of a white sports coupe on a tree-lined road"></div>
    <div class="bid">Buy it now for £13750 or please bid &raquo;</div>
    <h3>Velmont Tessa</h3>
    <div class="specs"><span>2014 - 64</span><span>White</span><span>86000 Miles</span><span>Ridgeway Cars</span><span>Automatic</span><span>127 Miles Away</span></div>
    <div class="deal"><h4>Trying to deal my customer</h4><p style="top:34px">Trade Price : £15,750</p><p style="top:52px">Retail Price : £17,750</p><div class="btn">More Info</div></div>
  </article>

  <section class="promo" role="img" aria-label="Dark blurred photograph of a road at night">
    <h2 class="heading">Buying &amp; Selling just got easier!</h2>
    <p>List your stock in minutes and reach trusted trade buyers across the country. Every dealer is checked before joining, so you trade only with real businesses. Simple tools, clear prices and fast replies help you move cars sooner and keep your forecourt fresh every week.</p>
    <div class="contact-box" style="left:425px">Call the customer support
      <div class="val"><svg width="8" height="11" viewBox="0 0 8 11"><rect x="0.5" y="0.5" width="7" height="10" rx="1" fill="none" stroke="#f5d30f"/><circle cx="4" cy="8.5" r=".8" fill="#f5d30f"/></svg>0123 555 019</div></div>
    <div class="contact-box" style="left:606px">Send us a message
      <div class="val"><svg width="11" height="8" viewBox="0 0 11 8"><rect width="11" height="8" fill="#f5d30f"/><path d="M0 0l5.5 4.5L11 0" stroke="#151515" fill="none"/></svg>contact@motorbayhub.com</div></div>
  </section>

  <h2 class="section-title heading" style="top:1380px">Customer Service - Contact Us</h2>
  <div class="form-label">Send a message</div>
  <div class="input" style="top:1466px">Name *</div>
  <div class="input" style="top:1513px">Email *</div>
  <div class="input" style="top:1560px">Phone *</div>
  <div class="input textarea">Message</div>
  <div class="btn" style="left:610px;top:1560px;width:113px;height:31px">Send Message
    <svg width="9" height="8" viewBox="0 0 9 8"><path d="M1 1l3 3-3 3M5 1l3 3-3 3" stroke="#1b1b1b" stroke-width="1.4" fill="none"/></svg></div>

  <section class="testimonial" role="img" aria-label="Yellow-tinted photograph of hands typing on a keyboard">
    <h2 class="heading">Great thing people are saying about us</h2>
    <div class="quote-mark">&ldquo;</div>
    <p>Since we joined, selling trade cars has become quick and easy. We list a vehicle in the morning and often agree a deal by the afternoon. The buyers are genuine dealers, the prices are fair and the support team always answers fast. It saves our staff hours every week and keeps our stock moving. We would not go back to the old way of trading now that everything sits in one clear place.</p>
    <p class="who">Northline Motors<br>Australia</p>
  </section>

  <svg class="footer-top" width="1200" height="256" viewBox="0 0 1200 256"><polygon points="0,0 420,0 460,22 1200,22 1200,256 0,256" fill="var(--dark)"/></svg>
  <div class="footer-brand">Motorbayhub.com</div>
  <p class="footer-text">A trade-only marketplace built for car dealers who want simple tools. Post your stock, set a trade price and let other dealers bid or buy now. No clutter, no private sellers and no hidden fees. Our team checks every account so each deal is safe, fast and fair for both sides of the trade. Join today and start listing your first cars within minutes.</p>
  <div class="btn" style="left:160px;top:2143px;width:70px;height:19px;font-size:10px">Read More</div>
  <div class="footer-heading">Keep in touch</div>
  <div class="f-input" style="left:664px;width:176px">Your Name *</div>
  <div class="f-input" style="left:858px;width:182px">Your Email *</div>
  <div class="btn" style="left:664px;top:2092px;width:81px;height:33px;font-weight:700">Submit
    <svg width="9" height="8" viewBox="0 0 9 8"><path d="M1 1l3 3-3 3M5 1l3 3-3 3" stroke="#1b1b1b" stroke-width="1.4" fill="none"/></svg></div>
  <p class="signup-note">Sign up now to get the latest news, deals and information</p>

  <footer class="bottom-bar">
    <nav class="foot-nav"><a href="#">Home</a><a href="#">Who we are</a><a href="#">Cars for sale</a><a href="#">News &amp; Reviews</a><a href="#">Help</a></nav>
    <div class="copyright">&copy; 2015 motorbayhub.com, inc. All Rights Reserved.</div>
    <div class="social"><span></span><span></span><span></span><span></span></div>
  </footer>

</div>
</body>
</html>
```